Web Page Design for a Website that Provides Tutoring

I am looking to create an online tutoring website. The website will allow parents or students to contact tutors with a view to instructing them to tutor themselves or their children.

The name of the website is LendYourLessons.

This brief is to create the design for one of the web pages for this web site. I am hoping the same designer will be available to design other pages.

The page I want designed is one of the more complex and I have attached the design as an excel spreadsheet. The web page needs to include all the items on this page but if you want to change the positioning of the items then Im fine with that.

I recently had two logos created for this website. My favourite is the one with a mortar board but im not sure I like the colours. I have attached both of these logos and you can use either of them, change the colours or create something different. I just want a design pleasing to the eye. If the logo is changed I would like that in a seperate file.

So can you please submit designs for this page. I have attached the two logos which you can use, change or if you feel you have a better idea then you can use that.

On the spreadsheet the Send Message, Favourite etc are buttons.

Target Market(s)

People who want to better themselves.
Possible middle class to upper class.

Industry/Entity Type

Tutoring

Number of Pages Required

1 page

Requirements
Must have
• The designs must have alot of the information attached in the spreadsheet.

```html
<!DOCTYPE html>
<html lang="en">
<head>
<meta charset="utf-8">
<title>LendYourLessons – Tutor Profile</title>
<link href="https://fonts.googleapis.com/css2?family=Lato:wght@400;700;900&display=swap" rel="stylesheet">
<style>
:root{
  --orange:#f7941d;
  --nav:#00aeef;
  --nav-active:#2e5a9a;
  --pale:#d6e0f5;
  --ink-blue:#1a7bb9;
  --ink:#222;
  --grey-box:#dcdcdc;
  --line:#c9c9c9;
  --footer:#2f5597;
  --white:#fff;
}
*{box-sizing:border-box;margin:0;padding:0}
html,body{width:693px;height:1200px;overflow:hidden}
body{font-family:"Lato",sans-serif;color:var(--ink);background:var(--white);position:relative}
.abs{position:absolute}

/* header */
.brand{left:66px;top:12px;display:flex;align-items:center;gap:6px;font-size:24px;font-weight:700;color:var(--orange)}
.brand-mark{width:16px;height:16px;background:var(--orange)}
.user-links{left:520px;top:7px;font-size:11px;font-weight:700;color:var(--nav-active);display:flex;gap:10px}
.user-links span+span{border-left:1px solid var(--nav-active);padding-left:10px}
.search-box{left:448px;top:27px;width:110px;height:20px;border:1px solid #999;font-size:8px;color:#777;padding:5px 7px}
.search-btn{left:562px;top:27px;width:50px;height:20px;background:var(--orange);color:var(--white);font-size:9.5px;font-weight:700;text-align:center;line-height:20px}

/* nav */
.main-nav{left:0;top:54px;width:693px;height:32px;background:var(--nav);display:flex;padding-left:66px}
.main-nav a{width:110px;height:32px;line-height:32px;text-align:center;color:var(--white);font-size:11px;font-weight:700;text-decoration:none;border-right:1px solid rgba(255,255,255,.6)}
.main-nav a:first-child{border-left:1px solid rgba(255,255,255,.6)}
.main-nav a.active{background:var(--nav-active)}

/* hero */
.hero{left:0;top:86px;width:693px;height:168px;background:linear-gradient(100deg,#5b5b5b,#9a9a9a 40%,#c9c9c9 70%,#7d7d7d)}
.avatar{left:206px;top:132px;width:80px;height:80px;border-radius:50%;background:linear-gradient(#caa58c,#8b6b5a);border:2px solid #eee}
.tutor-name{left:308px;top:143px;font-size:12px;font-weight:700;color:var(--orange)}
.tutor-title{left:308px;top:163px;font-size:12.5px;color:var(--white)}
.status{left:308px;top:185px;display:flex;align-items:center;gap:8px;font-size:12px;color:var(--white)}
.toggle{width:26px;height:13px;border-radius:7px;background:#3aa34a;position:relative}
.toggle::after{content:"";position:absolute;right:2px;top:2px;width:9px;height:9px;border-radius:50%;background:var(--white)}

/* profile */
.card{background:var(--white);border:1px solid var(--line);box-shadow:0 0 3px rgba(0,0,0,.15)}
.side-card{left:65px;top:273px;width:181px;height:108px}
.side-card h3{background:var(--pale);height:28px;line-height:28px;padding-left:16px;font-size:10px;color:var(--ink-blue)}
.rate{position:absolute;left:15px;top:42px;width:88px;height:22px;background:var(--orange);color:var(--white);font-size:10px;font-weight:700;text-align:center;line-height:22px}
.share-row{position:absolute;left:16px;top:76px;display:flex;gap:2px}
.share-row span,.foot-share span{display:block;background:var(--nav-active)}
.share-row span{width:11px;height:11px}
.tab{left:258px;top:252px;width:60px;height:21px;background:var(--white);border:1px solid var(--line);border-bottom:none;border-radius:3px 10px 0 0;font-size:7px;color:#555;text-align:center;line-height:20px}
.intro-card{left:258px;top:273px;width:355px;height:108px;padding:13px 10px}
.intro-card h2{font-size:10px;color:var(--ink-blue);margin-bottom:8px}
.intro-card p{font-size:7px;line-height:11px;margin-bottom:7px}
.learn{position:absolute;right:11px;bottom:19px;font-size:6.5px;color:var(--ink-blue);text-decoration:underline;font-weight:700}
.action{top:392px;width:93px;height:23px;background:var(--orange);color:var(--white);font-size:9.5px;font-weight:700;text-align:center;line-height:23px}

/* dark band */
.room{left:0;top:424px;width:693px;height:298px;background:linear-gradient(#3e4a63,#4b5672 45%,#6e6a64 75%,#d8d8dc)}
.info-box{background:var(--white);border:2px solid #e9ecf3}
.info-head{height:30px;background:var(--pale);position:relative}
.info-head span{position:absolute;top:9px;font-size:9px;font-weight:700;color:var(--ink-blue)}
.grey{position:absolute;background:var(--grey-box);font-size:7px;padding:9px 0 0 8px;line-height:13px}
.grey li{list-style:none;position:relative;padding-left:9px}
.grey li::before{content:"";position:absolute;left:0;top:5px;width:4px;height:4px;border-radius:50%;background:var(--orange)}
.section-title{font-size:13px;font-weight:900;letter-spacing:.2px}

/* availability */
.avail{left:66px;top:773px;width:547px;border-collapse:collapse;font-size:7.5px;border:1px solid var(--line)}
.avail th{background:var(--pale);height:29px;color:var(--ink-blue);font-size:9px;border-right:1px solid var(--white)}
.avail td{height:23.5px;border:1px solid #ddd}
.avail td:first-child{padding-left:14px}
.avail tr:nth-child(even) td{background:var(--pale)}
.select{display:flex;width:50px;height:17px;border:1px solid #6b8fd0;background:var(--white);margin:0 auto;align-items:center}
.select b{flex:1;text-align:center;font-size:7px}
.select i{width:14px;height:15px;background:var(--pale);border-left:1px solid #6b8fd0;position:relative}
.select i::after{content:"";position:absolute;left:3px;top:5px;border:4px solid transparent;border-top:6px solid var(--nav-active)}

/* reviews */
.library{left:0;top:942px;width:693px;height:222px;background:linear-gradient(#4a3a32,#6b5444 40%,#55443a 70%,#3a2e28)}
.faint-title{left:66px;top:952px;font-size:13px;font-weight:900;color:rgba(40,40,40,.45)}
.reviews{left:64px;top:982px;width:550px;border-collapse:collapse;background:var(--white);font-size:7.5px}
.reviews th{background:var(--pale);height:31px;color:var(--ink-blue);font-size:9px;text-align:left;padding-left:14px}
.reviews th:nth-child(3){text-align:center;padding-left:0}
.reviews td{height:24px;padding-left:14px;border-right:1px solid #ccc;border-top:1px solid #ccc}
.reviews tr:nth-child(odd) td{background:var(--pale)}
.reviews td.stars{color:var(--orange);text-align:center;padding-left:0;font-size:9px;letter-spacing:-1px}

/* footer */
.site-footer{left:0;top:1164px;width:693px;height:36px;background:var(--footer);color:var(--white);font-size:9.5px;font-weight:700;padding:13px 66px}
.foot-share{position:absolute;left:528px;top:9px;display:flex;gap:5px}
.foot-share span{width:18px;height:18px;background:var(--orange)}
</style>
</head>
<body>

<header>
  <div class="abs brand"><span class="brand-mark"></span>LendYourLessons</div>
  <div class="abs user-links"><span>Hi Jane</span><span>Logout</span></div>
  <div class="abs search-box">Subject (ex: algebra)</div>
  <div class="abs search-btn">Search</div>
</header>

<nav class="abs main-nav">
  <a class="active" href="#">HOME</a><a href="#">STUDENT</a><a href="#">TUTOR</a><a href="#">ABOUT</a><a href="#">CONTACT</a>
</nav>

<section>
  <div class="abs hero" role="img" aria-label="Greyscale photo of a hand writing with a pen on paper"></div>
  <div class="abs avatar" role="img" aria-label="Portrait photo of the tutor"></div>
  <div class="abs tutor-name">Jane D,</div>
  <div class="abs tutor-title">Professional English Tutor</div>
  <div class="abs status"><span class="toggle"></span>Jane D, is available.</div>
</section>

<section>
  <div class="abs card side-card">
    <h3>Piccle</h3>
    <div class="rate">25 USD / hour</div>
    <div class="share-row"><span></span><span></span><span></span><span></span></div>
  </div>
  <div class="abs tab">Profile</div>
  <div class="abs card intro-card">
    <h2>Introduction</h2>
    <p>My name is Jane and I am professional English tutor. This in an example profile and this is dummy content.</p>
    <p>Please contact me to discuses your goals and your availablity for lessons.</p>
    <span class="learn">Learn more</span>
  </div>
  <div class="abs action" style="left:282px">Send Message</div>
  <div class="abs action" style="left:390px">Favour Tutor</div>
  <div class="abs action" style="left:497px">Write Review</div>
</section>

<section>
  <div class="abs room" role="img" aria-label="Photo of four interview panel members seated at a table"></div>
  <div class="abs info-box" style="left:63px;top:438px;width:551px;height:104px">
    <div class="info-head">
      <span style="left:39px">Tutoring type</span><span style="left:135px">Teacher</span><span style="left:230px">Willing to Travel</span><span style="left:325px">Age</span><span style="left:420px">DBS (CRB)</span>
    </div>
    <ul class="grey" style="left:39px;top:34px;width:89px;height:62px"><li>In personal only</li><li>Home Only</li></ul>
    <ul class="grey" style="left:135px;top:34px;width:89px;height:62px"><li>Full Time Tutor</li><li>Full Time Student</li></ul>
    <ul class="grey" style="left:230px;top:34px;width:89px;height:62px"><li>Yes</li><li>No</li></ul>
    <ul class="grey" style="left:325px;top:34px;width:89px;height:62px"><li>20 - 25</li><li>26 - 30</li></ul>
    <ul class="grey" style="left:420px;top:34px;width:89px;height:62px"><li></li><li></li></ul>
  </div>

  <h2 class="abs section-title" style="left:65px;top:575px;color:var(--white)">SUBJECTS TAUGHTS</h2>
  <div class="abs info-box" style="left:64px;top:606px;width:550px;height:104px">
    <div class="info-head">
      <span style="left:38px">Primary</span><span style="left:118px">Secondary</span><span style="left:197px">GCSE</span><span style="left:277px">A-level</span><span style="left:356px">University</span><span style="left:437px">Adult Learner</span>
    </div>
    <ul class="grey" style="left:38px;top:34px;width:73px;height:62px"><li>Biology £20</li><li>Chemistry £20</li></ul>
    <ul class="grey" style="left:118px;top:34px;width:73px;height:62px"><li></li><li></li></ul>
    <ul class="grey" style="left:197px;top:34px;width:73px;height:62px"><li>£25</li><li>£25</li></ul>
    <ul class="grey" style="left:277px;top:34px;width:73px;height:62px"><li>£30</li><li>£30</li></ul>
    <ul class="grey" style="left:356px;top:34px;width:73px;height:62px"><li></li><li></li></ul>
    <ul class="grey" style="left:437px;top:34px;width:73px;height:62px"><li></li><li></li></ul>
  </div>
</section>

<section>
  <h2 class="abs section-title" style="left:66px;top:741px">AVAILABILITY</h2>
  <table class="abs avail">
    <colgroup><col style="width:57px"><col style="width:59px"><col style="width:59px"><col style="width:61px"><col style="width:62px"><col style="width:64px"><col style="width:62px"><col style="width:61px"><col style="width:62px"></colgroup>
    <tr><th></th><th>Monday</th><th>Tuesday</th><th>Wednesday</th><th>Thursday</th><th>Friday</th><th>Saturday</th><th>Sunday</th><th></th></tr>
    <tr><td>7 to 8</td><td></td><td></td><td></td><td></td><td></td><td></td><td></td><td><div class="select"><b>NO</b><i></i></div></td></tr>
    <tr><td>8 to 9</td><td></td><td></td><td></td><td></td><td></td><td></td><td></td><td><div class="select"><b>NO</b><i></i></div></td></tr>
    <tr><td>4 to 5</td><td></td><td></td><td></td><td></td><td></td><td></td><td></td><td><div class="select"><b>NO</b><i></i></div></td></tr>
    <tr><td>5 to 6</td><td></td><td></td><td></td><td></td><td></td><td></td><td></td><td><div class="select"><b>NO</b><i></i></div></td></tr>
    <tr><td>7 to 8</td><td></td><td></td><td></td><td></td><td></td><td></td><td></td><td></td></tr>
  </table>
</section>

<section>
  <div class="abs library" role="img" aria-label="Photo of library bookshelves filled with books"></div>
  <h2 class="abs faint-title">TUTOR SHARE REVIEW</h2>
  <table class="abs reviews">
    <colgroup><col style="width:114px"><col style="width:125px"><col style="width:72px"><col></colgroup>
    <tr><th>Tutee Name</th><th>Date / Time of Review</th><th>Rating</th><th>Comments</th></tr>
    <tr><td>Nick</td><td>12 Dec 2016 04:30 PM</td><td class="stars">★★★★★</td><td>Thank you.</td></tr>
    <tr><td>Watson</td><td>12 Dec 2016 04:30 PM</td><td class="stars">★★★★★</td><td>Awsome Instructor.</td></tr>
    <tr><td>Bella</td><td>12 Dec 2016 04:30 PM</td><td class="stars">★★★★★</td><td>Very Thankful to you.</td></tr>
    <tr><td>Tara Swann</td><td>12 Dec 2016 04:30 PM</td><td class="stars">★★★★★</td><td>Thank you.</td></tr>
    <tr><td>Jack</td><td>12 Dec 2016 04:30 PM</td><td class="stars">★★★★★</td><td>Awsome Instructor.</td></tr>
  </table>
</section>

<footer class="abs site-footer">
  Copyright 2016.
  <div class="foot-share"><span></span><span></span><span></span><span></span></div>
</footer>

</body>
</html>
```